Simple and Approachable Cover for Pet Expo Company Page

Size: 2000 x 430; looking simply for words "Tenbury HR Consulting" and email address "TenburyHRConsulting@mailvane.com." This is for a cover photo for a company profile page for the Northway Animal Fair, where I am a featured speaker on Employee Communications later this month. You can incorporate the attached photo to the left of the banner ad if you wish. The mood I wish to present is approachable, positive and simple.

Target Market(s)

small pet retail business owners

Industry/Entity Type

Pet Shop

Font styles to use
Serif
Sans Serif

Requirements
Must have
• Email address clearly defined/separated. Easy to read.
Nice to have
• I like the picture that I included; subtle pet paw background is also nice
Should not have
• No paid stock images

```html
<!DOCTYPE html>
<html lang="en">
<head>
<meta charset="utf-8">
<title>Tenbury HR Consulting – Cover Banner</title>
<link rel="stylesheet" href="https://fonts.googleapis.com/css2?family=Yeseva+One&family=Open+Sans:wght@400&display=swap">
<style>
  :root {
    --page-bg: #f4f7f8;
    --banner-bg: #cfd0d2;
    --brand-purple: #7b2a80;
    --soft-lilac: #e6d3ea;
    --soft-white: #f1f2f4;
    --ink: #151515;
    --photo-dark: #2a2a2a;
    --photo-mid: #555657;
  }
  * { margin: 0; padding: 0; box-sizing: border-box; }
  html, body {
    width: 1200px;
    height: 1000px;
    overflow: hidden;
    background: var(--page-bg);
  }
  .canvas {
    position: relative;
    width: 1200px;
    height: 1000px;
  }
  .cover-banner {
    position: absolute;
    left: 21px;
    top: 376px;
    width: 1159px;
    height: 249px;
    background: var(--banner-bg);
    overflow: hidden;
  }
  .callout-art {
    position: absolute;
    left: 14px;
    top: 16px;
    width: 190px;
    height: 170px;
    border-radius: 12px;
    background: radial-gradient(ellipse at 50% 50%, var(--soft-white) 0%, var(--soft-white) 45%, var(--soft-lilac) 80%, var(--banner-bg) 100%);
  }
  .pet-photo {
    position: absolute;
    left: 195px;
    top: 44px;
    width: 200px;
    height: 205px;
    border-radius: 90px 90px 0 0;
    background: radial-gradient(ellipse at 50% 35%, var(--photo-mid) 0%, var(--photo-dark) 60%, #1d1d1d 100%);
  }
  .brand-name {
    position: absolute;
    right: 57px;
    top: 52px;
    font-family: "Yeseva One", Georgia, serif;
    font-weight: 400;
    font-size: 50px;
    line-height: 1.2;
    letter-spacing: 1.5px;
    color: var(--brand-purple);
    white-space: nowrap;
  }
  .contact-email {
    position: absolute;
    right: 57px;
    top: 150px;
    font-family: "Open Sans", Arial, sans-serif;
    font-size: 34px;
    line-height: 1.2;
    letter-spacing: 0.3px;
    color: var(--ink);
    white-space: nowrap;
  }
</style>
</head>
<body>
  <main class="canvas">
    <section class="cover-banner">
      <div class="callout-art" role="img" aria-label="Decorative speech-bubble illustration with an exclamation, in white with a soft purple glow"></div>
      <div class="pet-photo" role="img" aria-label="Photo of a small black pug looking up toward the speech bubble"></div>
      <h1 class="brand-name">Tenbury HR Consulting</h1>
      <p class="contact-email">TenburyHRConsulting@mailvane.com</p>
    </section>
  </main>
</body>
</html>
```